Business Card Design

Non-profit organization creating opportunities for:
Personal empowerment
Community Outreach
Healthier Life Choices
Body/Mind/Spirit Nourishment
Emotional Transformation
Charity & Network Opportunities
Everyday people making An extrodinary sufferance
All achieved from the Source within YOU.
Organization logo is the ying yang symbol with a small circle above it as if it were the head and the ying yang symbol was the body.  Also in side upper ying needs to be a heart and in the lower yang needs to be the letter C. This is very important as it came to me in a dream n the forming of this organization.  Color choice is open although a thought I hade was that the heart is red metallic foil (sine a red heart is the symbol of love)and the c is gold foil( the gifts of the 3 wise men and gold being one of them).a verticle card is preferred and logo as large as possible on it even if ying yang is made oval Ilook forward to the layouts and designs you can come up with.

Contact Information for Business Card
Lumen Harbor. Org
Paul Marsky
Executive Director
Lumen harbor.paul@brindlemail.com
512-394-2086

```html
<!DOCTYPE html>
<html lang="en">
<head>
<meta charset="utf-8">
<title>Lumen Harbor — Business Card</title>
<link rel="stylesheet" href="https://fonts.googleapis.com/css2?family=Questrial&family=Didact+Gothic&display=swap">
<style>
  :root {
    --backdrop: #e9e6e1;
    --teal-light: #35a68b;
    --teal-dark: #1d7763;
    --navy: #1f2a38;
    --orange: #f0981f;
    --ink-soft: #27343f;
    --chip: #d9dde0;
    --ray: rgba(255,255,255,0.10);
  }
  * { box-sizing: border-box; margin: 0; padding: 0; }
  html, body { width: 1200px; height: 723px; overflow: hidden; }
  body {
    background: var(--backdrop);
    display: flex;
    align-items: center;
    justify-content: center;
    gap: 54px;
    font-family: "Questrial", "Didact Gothic", sans-serif;
  }
  .card {
    width: 343px;
    height: 600px;
    border-radius: 14px;
    border: 7px solid var(--navy);
    background: linear-gradient(160deg, var(--teal-light), var(--teal-dark));
    overflow: hidden;
    box-shadow: 0 6px 18px rgba(0,0,0,0.18);
  }
  .card svg { display: block; width: 100%; height: 100%; }
  .wordmark { font-family: "Questrial", sans-serif; fill: var(--navy); }
  .person-name { font-family: "Questrial", sans-serif; font-variant: small-caps; fill: var(--navy); letter-spacing: 1px; }
  .person-role { font-family: "Didact Gothic", sans-serif; fill: var(--navy); }
  .band { fill: none; stroke: var(--orange); }
  .band-text { font-family: "Didact Gothic", sans-serif; font-weight: 700; fill: var(--navy); letter-spacing: 1.5px; }
  .contact-chip { fill: var(--chip); }
  .chip-letter { font-family: "Didact Gothic", sans-serif; font-size: 9px; fill: var(--navy); text-anchor: middle; }
  .contact-text { font-family: "Didact Gothic", sans-serif; font-size: 13px; fill: var(--ink-soft); }
</style>
</head>
<body>

  <!-- Front of card -->
  <div class="card card-front">
    <svg viewBox="0 0 329 586" xmlns="http://www.w3.org/2000/svg">
      <circle cx="70" cy="78" r="34" fill="var(--navy)"/>
      <text class="wordmark" x="116" y="86" font-size="24">Lumen Harbor</text>

      <text class="person-name" x="34" y="170" font-size="32">Paul Marsky</text>
      <text class="person-role" x="36" y="192" font-size="15">Executive Director</text>

      <path id="band-top" class="band" stroke-width="18" d="M -10 250 Q 160 262 340 300"/>
      <text class="band-text" font-size="13" dy="5">
        <textPath href="#band-top" startOffset="54%">LUMEN HARBOR</textPath>
      </text>

      <g class="contacts">
        <circle class="contact-chip" cx="30" cy="326" r="7"/>
        <text class="chip-letter" x="30" y="329">W</text>
        <text class="contact-text" x="46" y="331">lumenharbor.org</text>

        <circle class="contact-chip" cx="30" cy="349" r="7"/>
        <text class="chip-letter" x="30" y="352">E</text>
        <text class="contact-text" x="46" y="354">harbor.paul@brindlemail.com</text>

        <circle class="contact-chip" cx="30" cy="372" r="7"/>
        <text class="chip-letter" x="30" y="375">C</text>
        <text class="contact-text" x="46" y="377">512-394-2086</text>
      </g>

      <path id="band-bottom" class="band" stroke-width="20" d="M -10 398 Q 150 418 340 452"/>
      <text class="band-text" font-size="14" dy="5">
        <textPath href="#band-bottom" startOffset="8%">CREATING OPPORTUNITIES</textPath>
      </text>
    </svg>
  </div>

  <!-- Back of card -->
  <div class="card card-back">
    <svg viewBox="0 0 329 586" xmlns="http://www.w3.org/2000/svg">
      <defs>
        <radialGradient id="fan-glow" cx="0" cy="1" r="1">
          <stop offset="0" stop-color="var(--ray)" stop-opacity="0"/>
          <stop offset="0.85" stop-color="#ffffff" stop-opacity="0.10"/>
          <stop offset="1" stop-color="#ffffff" stop-opacity="0"/>
        </radialGradient>
      </defs>
      <path role="img" aria-label="Soft radiating fan of light rays" d="M 0 586 L 0 330 A 256 256 0 0 1 256 586 Z" fill="url(#fan-glow)"/>

      <circle cx="172" cy="190" r="132" fill="var(--navy)"/>
      <text class="wordmark" x="28" y="400" font-size="29" letter-spacing="1">LUMEN HARBOR</text>
    </svg>
  </div>

</body>
</html>
```